" Somos uma empresa jovem que desenvolve sites e sistemas focado em imobiliárias e afins. Buscando oferecer as melhores ferramentas para a administraçao e divulgaçao dos imóveis para os nossos clientes. "

```html
<!DOCTYPE html>
<html lang="pt-BR">
<head>
<meta charset="utf-8">
<title>KVR – Cartão de visita</title>
<link href="https://fonts.googleapis.com/css2?family=Archivo:wght@400;600;800&display=swap" rel="stylesheet">
<style>
  :root{
    --page:#e9e9e6;
    --white:#ffffff;
    --green:#2f8a1e;
    --green-dark:#1f6512;
    --green-light:#4fae32;
    --text-light:#eaf6e4;
  }
  *{margin:0;padding:0;box-sizing:border-box}
  html,body{width:1200px;height:1200px;overflow:hidden}
  body{background:var(--page);font-family:"Archivo",Arial,sans-serif;position:relative}
  .card{position:absolute;left:180px;width:840px;height:466px;border-radius:4px;overflow:hidden;box-shadow:0 6px 20px rgba(0,0,0,.15)}
  .card-front{top:100px;background:var(--white)}
  .card-back{top:634px;background:linear-gradient(160deg,var(--green-light) 0%,var(--green) 45%,var(--green-dark) 100%)}

  .brand{position:absolute;left:0;right:0;top:140px;display:flex;align-items:center;justify-content:center;gap:22px}
  .brand-dot{width:64px;height:64px;border-radius:50%;background:var(--green)}
  .brand-block{display:flex;flex-direction:column}
  .brand-name{font-weight:800;font-size:84px;line-height:1;color:var(--green);letter-spacing:2px}
  .brand-tagline{font-size:11px;font-weight:600;color:var(--green);letter-spacing:1.5px;margin-top:4px}

  .front-band{position:absolute;left:0;right:0;bottom:0;height:92px}
  .front-band svg{position:absolute;inset:0}
  .front-url{position:absolute;right:90px;bottom:22px;color:var(--white);font-weight:800;font-size:26px;letter-spacing:.5px}

  .back-accent{position:absolute;left:-120px;top:40px;width:460px;height:460px;border-radius:50%;background:rgba(255,255,255,.08)}
  .person{position:absolute;left:470px;top:70px;color:var(--white)}
  .person-name{font-size:30px;font-weight:400}
  .person-role{font-size:17px;color:var(--text-light);margin-top:4px}

  .contacts{position:absolute;left:470px;top:205px;list-style:none;color:var(--white);font-size:21px}
  .contacts li{display:flex;align-items:center;gap:14px;height:34px}
  .icon{width:20px;height:20px;flex:none}
  .icon-dot{width:16px;height:16px;margin:0 2px;border-radius:50%;background:var(--white);flex:none}
</style>
</head>
<body>

<section class="card card-front">
  <div class="brand">
    <span class="brand-dot"></span>
    <div class="brand-block">
      <span class="brand-name">KVR</span>
      <span class="brand-tagline">SITES E SISTEMAS IMOBILIÁRIOS</span>
    </div>
  </div>
  <div class="front-band">
    <svg viewBox="0 0 840 92" preserveAspectRatio="none" aria-hidden="true">
      <path d="M0 20 H50 Q60 20 66 8 Q70 0 80 0 H760 Q770 0 774 8 Q780 20 790 20 H840 V92 H0 Z" fill="var(--green)"/>
    </svg>
    <span class="front-url">www.kvr.com.br</span>
  </div>
</section>

<section class="card card-back">
  <div class="back-accent"></div>
  <div class="person">
    <p class="person-name">Nome do funcionário</p>
    <p class="person-role">Cargo na empresa</p>
  </div>
  <ul class="contacts">
    <li>
      <svg class="icon" viewBox="0 0 24 24" aria-hidden="true"><path fill="#fff" d="M6.6 10.8a15 15 0 0 0 6.6 6.6l2.2-2.2a1 1 0 0 1 1-.25 11.4 11.4 0 0 0 3.6.57 1 1 0 0 1 1 1V20a1 1 0 0 1-1 1A17 17 0 0 1 3 4a1 1 0 0 1 1-1h3.5a1 1 0 0 1 1 1c0 1.25.2 2.45.57 3.6a1 1 0 0 1-.25 1z"/></svg>
      48 32 4150.2286
    </li>
    <li>
      <svg class="icon" viewBox="0 0 24 24" aria-hidden="true"><circle cx="12" cy="12" r="9" fill="none" stroke="#fff" stroke-width="2"/><path d="M3 12h18M12 3c3 3 3 15 0 18M12 3c-3 3-3 15 0 18" fill="none" stroke="#fff" stroke-width="1.6"/></svg>
      www.kvr.com.br
    </li>
    <li>
      <svg class="icon" viewBox="0 0 24 24" aria-hidden="true"><rect x="3" y="5" width="18" height="14" rx="2" fill="none" stroke="#fff" stroke-width="2"/><path d="M3 7l9 6 9-6" fill="none" stroke="#fff" stroke-width="2"/></svg>
      contato@kvr.com.br
    </li>
    <li><span class="icon-dot"></span>kvr.social</li>
    <li><span class="icon-dot"></span>kvr.rede</li>
  </ul>
</section>

</body>
</html>
```